salami paper bag design The size is 10.5cm 21.5cm 6.7cm

This time we need to make renew salami package design. Planning to make paper salami package. I tried to design but I couldnt formyself.
So please correct my design and recreate more nicer package design from my salami design that attach on the documents.
Logo part I am planning gold stamp. If anybody can make more nicer logo for the package,I don’t mind it.please change the color and shape and everything.
The size is 10.5cm 21.5cm 6.7cm
Thank you.

Target Market(s)

uper market make costomer feel luxurious

Industry/Entity Type

salami matured meat products

Font styles to use
Sans Serif
Decorative
Script

Colors

Designer to choose colors to be used in the design.

Requirements
Nice to have
• Make customer feel joy for genuine fermented salami with wine
Should not have
• My projrct must not have cheap discount design.

```html
<!DOCTYPE html>
<html lang="en">
<head>
<meta charset="utf-8">
<title>Koridan Artisan – Handmade Salami Box Dieline</title>
<link rel="stylesheet" href="https://fonts.googleapis.com/css2?family=Josefin+Sans:wght@600;700&family=Noto+Sans+JP:wght@700&display=swap">
<style>
  :root {
    --backdrop: #e6e6e6;
    --paper: #eaf2fa;
    --lavender: #b4a5d1;
    --peach: #f6bc90;
    --coral: #f09294;
    --ink: #111111;
    --window-light: #f1f0ec;
    --window-dark: #b9a9a0;
  }
  html, body {
    margin: 0;
    width: 1200px;
    height: 1200px;
    overflow: hidden;
    background: var(--backdrop);
  }
  .canvas {
    width: 1200px;
    height: 1200px;
    display: flex;
    align-items: center;
    justify-content: center;
  }
  .dieline { display: block; }
  .paper { fill: var(--paper); }
  .peach { fill: var(--peach); }
  .coral { fill: var(--coral); }
  .lavender { fill: var(--lavender); }
  .brand-name {
    font-family: "Josefin Sans", sans-serif;
    font-weight: 700;
  }
  .brand-sub {
    font-family: "Josefin Sans", sans-serif;
    font-weight: 600;
  }
  .product-title {
    font-family: "Josefin Sans", sans-serif;
    font-weight: 700;
    fill: #ffffff;
    letter-spacing: 1px;
  }
  .tagline {
    font-family: "Josefin Sans", sans-serif;
    font-weight: 700;
    fill: var(--ink);
    letter-spacing: 1px;
  }
  .tagline-jp {
    font-family: "Noto Sans JP", sans-serif;
    font-weight: 700;
    fill: var(--ink);
  }
  .brand-mark { fill: none; stroke: var(--ink); stroke-width: 2; }
</style>
</head>
<body>
<main class="canvas">
  <svg class="dieline" width="1065" height="711" viewBox="80 103 1014 677" xmlns="http://www.w3.org/2000/svg">
    <defs>
      <linearGradient id="window-fill" x1="0" y1="0" x2="0.3" y2="1">
        <stop offset="0" stop-color="var(--window-light)"/>
        <stop offset="0.6" stop-color="#e2ddd6"/>
        <stop offset="1" stop-color="var(--window-dark)"/>
      </linearGradient>
      <clipPath id="front-clip"><rect x="271" y="295" width="632" height="293"/></clipPath>
      <clipPath id="bottom-clip"><rect x="271" y="588" width="632" height="192"/></clipPath>
    </defs>

    <!-- Top flap -->
    <g class="top-flap">
      <rect class="paper" x="271" y="103" width="632" height="192"/>
      <g transform="rotate(180 587 195)">
        <text class="tagline" x="587" y="185" text-anchor="middle" font-size="30">LIVING WITH FOOD</text>
        <text class="tagline-jp" x="587" y="222" text-anchor="middle" font-size="24">食べ物と一緒に暮らす</text>
      </g>
    </g>

    <!-- Side flaps -->
    <g class="side-flap side-flap--left">
      <rect class="paper" x="80" y="295" width="191" height="293"/>
      <g transform="translate(162 441) rotate(-90)">
        <text class="brand-name" x="0" y="0" text-anchor="middle" font-size="40" fill="var(--lavender)">Koridan</text>
        <text class="brand-sub" x="0" y="26" text-anchor="middle" font-size="16" fill="var(--lavender)">Artisan</text>
      </g>
    </g>
    <g class="side-flap side-flap--right">
      <rect class="paper" x="903" y="295" width="191" height="293"/>
      <g transform="translate(1000 441) rotate(90)">
        <text class="brand-name" x="0" y="0" text-anchor="middle" font-size="40" fill="var(--coral)">Koridan</text>
        <text class="brand-sub" x="0" y="26" text-anchor="middle" font-size="16" fill="var(--coral)">Artisan</text>
      </g>
    </g>

    <!-- Front panel -->
    <g class="front-panel" clip-path="url(#front-clip)">
      <rect class="peach" x="271" y="295" width="632" height="293"/>
      <path class="lavender" d="M271,295 H760 V495 C650,500 560,478 470,468 C390,460 320,482 271,486 Z"/>
      <path class="coral" d="M903,345 C855,372 815,432 760,452 C700,476 640,472 600,492 C556,514 556,560 596,588 H903 Z"/>
      <path class="paper" d="M271,295 H903 V345 C862,362 826,418 766,436 C706,454 640,430 570,434 C490,440 426,430 404,392 C382,344 330,300 271,302 Z"/>
      <circle class="brand-mark" cx="500" cy="370" r="26"/>
      <text class="brand-name" x="672" y="383" text-anchor="middle" font-size="40" fill="var(--ink)">Koridan</text>
      <text class="brand-sub" x="690" y="408" text-anchor="middle" font-size="16" fill="var(--ink)">Artisan</text>
      <text class="product-title" x="590" y="548" text-anchor="middle" font-size="38">HANDMADE SALAMI</text>
    </g>

    <!-- Bottom panel with product window -->
    <g class="bottom-panel" clip-path="url(#bottom-clip)">
      <rect class="peach" x="271" y="588" width="632" height="192"/>
      <path class="coral" d="M596,588 C640,650 650,710 700,780 H903 V588 Z"/>
      <rect class="product-window" x="415" y="588" width="290" height="192" rx="80" fill="url(#window-fill)" role="img" aria-label="Clear window showing white mould-coated salami sticks"/>
    </g>
  </svg>
</main>
</body>
</html>
```